Business Card Design - Local Discount Club

Looking for a fun business card for a local discount club. One side should be the logo only and the other should be have :

Name
Title
Phone, Email
Website

```html
<!DOCTYPE html>
<html lang="en">
<head>
<meta charset="utf-8">
<title>The Bayside Pass – Business Card</title>
<link href="https://fonts.googleapis.com/css2?family=Arimo:wght@400;700&display=swap" rel="stylesheet">
<style>
  :root {
    --backdrop: #dcdcdc;
    --card-white: #f6f6f7;
    --brand-blue: #3f5bbd;
    --brand-blue-dark: #3753b2;
    --brand-cyan: #3fd3e8;
    --brand-green: #97e26f;
    --icon-blue: #2f8fe0;
    --text-gray: #555a60;
    --divider: #b9bcc2;
  }
  * { margin: 0; padding: 0; box-sizing: border-box; }
  html, body {
    width: 1200px;
    height: 1200px;
    overflow: hidden;
  }
  body {
    position: relative;
    background: var(--backdrop);
    font-family: "Arimo", Arial, sans-serif;
  }
  .card {
    position: absolute;
    left: 262px;
    width: 686px;
    height: 392px;
    border-radius: 20px;
    overflow: hidden;
  }
  .card-front {
    top: 165px;
    background: var(--card-white);
  }
  .card-back {
    top: 653px;
    background: linear-gradient(180deg, #4362bd 0%, #3753b2 100%);
  }

  /* brand name lockup */
  .brand {
    position: absolute;
    display: flex;
    align-items: center;
    gap: 12px;
    font-weight: 700;
    white-space: nowrap;
  }
  .brand-dot {
    width: 18px;
    height: 18px;
    border-radius: 50%;
    flex: none;
  }
  .card-front .brand {
    left: 52px;
    top: 172px;
    font-size: 30px;
    color: var(--brand-blue);
  }
  .card-front .brand-dot { background: var(--brand-blue); }
  .card-back .brand {
    left: 50%;
    top: 50%;
    transform: translate(-50%, -50%);
    font-size: 42px;
    color: #ffffff;
  }
  .card-back .brand-dot { background: #ffffff; width: 22px; height: 22px; }

  .divider {
    position: absolute;
    left: 354px;
    top: 87px;
    width: 1px;
    height: 217px;
    background: var(--divider);
  }

  .contact {
    position: absolute;
    left: 382px;
    top: 100px;
    color: var(--text-gray);
  }
  .contact-name {
    font-size: 24px;
    font-weight: 700;
    color: var(--brand-blue);
    letter-spacing: 0.2px;
    line-height: 1.1;
  }
  .contact-title {
    font-size: 15.5px;
    margin-top: 2px;
  }
  .contact-address {
    font-size: 16.5px;
    line-height: 21px;
    margin-top: 14px;
  }
  .contact-list {
    list-style: none;
    margin-top: 12px;
    font-size: 16.5px;
    line-height: 21px;
  }
  .contact-list li {
    display: flex;
    align-items: center;
    gap: 8px;
  }
  .contact-list svg {
    width: 14px;
    height: 14px;
    flex: none;
    fill: var(--icon-blue);
  }

  .color-band {
    position: absolute;
    left: 0;
    bottom: 0;
    width: 686px;
    height: 11px;
  }
</style>
</head>
<body>

  <section class="card card-front" aria-label="Card front">
    <div class="brand"><span class="brand-dot"></span>The Bayside Pass</div>

    <div class="divider"></div>

    <div class="contact">
      <h1 class="contact-name">DANIEL MORROW</h1>
      <p class="contact-title">Managing Director</p>
      <p class="contact-address">412 Willow Court<br>Bridgeport, Maine 04120</p>
      <ul class="contact-list">
        <li>
          <svg viewBox="0 0 24 24" aria-hidden="true"><path d="M6.6 10.8a15.1 15.1 0 0 0 6.6 6.6l2.2-2.2c.3-.3.7-.4 1-.2 1.1.4 2.3.6 3.6.6.6 0 1 .4 1 1V20c0 .6-.4 1-1 1A17 17 0 0 1 3 4c0-.6.4-1 1-1h3.5c.6 0 1 .4 1 1 0 1.3.2 2.5.6 3.6.1.3 0 .7-.2 1z"/></svg>
          555-214-7730
        </li>
        <li>
          <svg viewBox="0 0 24 24" aria-hidden="true"><path d="M7 1h10a2 2 0 0 1 2 2v18a2 2 0 0 1-2 2H7a2 2 0 0 1-2-2V3a2 2 0 0 1 2-2zm0 3v14h10V4zm5 15.5a1 1 0 1 0 0 2 1 1 0 0 0 0-2z"/></svg>
          555-381-9046
        </li>
        <li>
          <svg viewBox="0 0 24 24" aria-hidden="true"><path d="M2 5h20v14H2zm2 2v.5l8 5.5 8-5.5V7zm0 2.9V17h16V9.9l-8 5.5z"/></svg>
          hello@baysidepass.com
        </li>
        <li>
          <svg viewBox="0 0 24 24" aria-hidden="true"><path d="M12 2a10 10 0 1 0 0 20 10 10 0 0 0 0-20zm-1 17.9A8 8 0 0 1 4.2 10.2L9 15v1c0 1.1.9 2 2 2zm6.9-2.5A2 2 0 0 0 16 16h-1v-3c0-.6-.4-1-1-1H8v-2h2c.6 0 1-.4 1-1V7h2a2 2 0 0 0 2-2v-.4a8 8 0 0 1 2.9 12.8z"/></svg>
          www.baysidepass.com
        </li>
      </ul>
    </div>

    <svg class="color-band" viewBox="0 0 686 11" preserveAspectRatio="none" aria-hidden="true">
      <polygon points="0,0 232,0 228,11 0,11" fill="var(--brand-blue)"/>
      <polygon points="232,0 466,0 462,11 228,11" fill="var(--brand-cyan)"/>
      <polygon points="466,0 686,0 686,11 462,11" fill="var(--brand-green)"/>
    </svg>
  </section>

  <section class="card card-back" aria-label="Card back">
    <div class="brand"><span class="brand-dot"></span>The Bayside Pass</div>
  </section>

</body>
</html>
```